Corvant Systems Business Card

Create an appealing and elegant Business card for corvant systems. Include logo and use related colors from website, be creative. Include Business name, my name, tile, address, contacts, address, and social media contacts if possible. Logo PSD file is attached.

Bleed Area: 3.46" x 2.32"
Trim: 3.3" x 2.16"
Safe Area: 3.14" x 2.02"

Save files as vector-based PDF with outlined text and PNG.
No crop marks
CMYK color setting

Business Card Info:

Corvant Systems

Dennis Halvorsen
Owner

512 Brindlemoor Rd Unit C
Linden Falls, VT 02871
t. 1.888.555.0162
e. dennis.h@corvantsys.example
w. www.corvantsys.example

facebook. www.facebook.com/CorvantSys
twitter. twitter.com/corvantsys
pinterest. www.pinterest.com/corvantsys/

Target Market(s)

Business Owners and Partners

Industry/Entity Type

Business

Requirements
Must have
• Logo and related colors from website

```html
<!DOCTYPE html>
<html lang="en">
<head>
<meta charset="utf-8">
<title>Corvant Systems Business Card</title>
<link rel="stylesheet" href="https://fonts.googleapis.com/css2?family=Open+Sans:wght@400;600;700&display=swap">
<style>
  :root {
    --backdrop: #e6e6e6;
    --paper: #fbfbfb;
    --ink: #111111;
    --charcoal: #232325;
    --steel-blue: #3f6590;
    --steel-blue-light: #5a7fa8;
    --white: #ffffff;
  }
  * { margin: 0; padding: 0; box-sizing: border-box; }
  html, body {
    width: 1200px; height: 720px; overflow: hidden;
    background: var(--backdrop);
    font-family: "Open Sans", Arial, sans-serif;
  }
  .canvas { position: relative; width: 1200px; height: 720px; }
  .card {
    position: absolute; top: 241px; width: 420px; height: 240px;
    overflow: hidden;
  }
  .card-front { left: 147px; background: var(--paper); }
  .card-back { left: 633px; }
  .card-shapes { position: absolute; inset: 0; }

  .holder-name {
    position: absolute; left: 79px; top: 20px;
    font-size: 32px; font-weight: 700; color: var(--white);
    letter-spacing: 1px; line-height: 1; white-space: nowrap;
  }
  .holder-title {
    position: absolute; left: 79px; top: 55px;
    font-size: 24px; font-weight: 400; color: var(--steel-blue);
    line-height: 1;
  }
  .brand-box {
    position: absolute; left: 2px; top: 98px; width: 142px; height: 129px;
    border: 2px solid var(--ink); background: var(--white);
    display: flex; align-items: center; justify-content: center; gap: 6px;
  }
  .brand-mark { width: 10px; height: 10px; background: var(--steel-blue); flex: none; }
  .brand-name { font-weight: 600; color: var(--ink); line-height: 1.05; }
  .brand-box .brand-name { font-size: 19px; }
  .contact-list {
    position: absolute; left: 191px; top: 122px;
    list-style: none; color: var(--white); font-size: 10px; line-height: 1;
  }
  .contact-list li { margin-bottom: 7px; white-space: nowrap; }
  .contact-list li.address { margin-bottom: 2px; }
  .contact-label { opacity: 0.75; margin-right: 2px; }

  .back-brand {
    position: absolute; inset: 0;
    display: flex; align-items: center; justify-content: center; gap: 12px;
  }
  .back-brand .brand-mark { width: 22px; height: 22px; }
  .back-brand .brand-name { font-size: 40px; text-align: left; white-space: nowrap; }
</style>
</head>
<body>
<main class="canvas">

  <section class="card card-front" aria-label="Business card front">
    <svg class="card-shapes" width="420" height="240" viewBox="0 0 420 240">
      <polygon class="name-band" points="58,11 420,11 420,94 22,94 22,39" fill="var(--charcoal)"/>
      <polygon class="contact-panel" points="146,98 395,98 395,199 365,227 146,227" fill="var(--steel-blue-light)"/>
    </svg>
    <h1 class="holder-name">Dennis Halvorsen</h1>
    <p class="holder-title">Owner</p>
    <div class="brand-box">
      <span class="brand-mark"></span>
      <span class="brand-name">Corvant<br>Systems</span>
    </div>
    <ul class="contact-list">
      <li><span class="contact-label">T.</span> 1.888.555.0162</li>
      <li><span class="contact-label">W.</span> www.corvantsys.example</li>
      <li><span class="contact-label">E.</span> dennis.h@corvantsys.example</li>
      <li class="address">512 Brindlemoor Rd Unit C</li>
      <li class="address">Linden Falls, VT 02871</li>
    </ul>
  </section>

  <section class="card card-back" aria-label="Business card back">
    <svg class="card-shapes" width="420" height="240" viewBox="0 0 420 240">
      <rect class="frame" x="0" y="0" width="420" height="240" fill="var(--charcoal)"/>
      <polygon class="corner-accent" points="0,0 50,0 0,48" fill="var(--steel-blue)"/>
      <polygon class="corner-accent" points="420,195 420,240 382,240" fill="var(--steel-blue)"/>
      <polygon class="inner-panel" points="50,7 406,7 406,191 371,233 14,233 14,54" fill="var(--paper)"/>
    </svg>
    <div class="back-brand">
      <span class="brand-mark"></span>
      <span class="brand-name">Corvant Systems</span>
    </div>
  </section>

</main>
</body>
</html>
```